PowerPoint Design Project

Design Brief
Corvanta is updating its stationary templates to reflect the company’s position as market leader in smart-location based solutions.
Using the existing Corvanta logo and corporate colours, create an engaging and visually appealing PowerPoint presentation template identity that works when printed on A4 and US Letter sized paper.
The successful designs will complement the current look and feel of the Corvanta website (www.corvanta-example.net) and communicate that Corvanta is a dynamic and modern technology company that is at the cutting edge of innovation.
Corvanta Brand
Corvanta stands for Precision Location Technology. The brand represents both a unique, highly innovative platform product and a mature consulting and support organisation dedicated to delivering solutions to blue-chip customer problems. The orange colour implies creativity while blue evokes trust and a rational approach. “Ubi” is Latin and means “where”, so the brand directly addresses the focus of the company: location. “Sense” can mean that we have sensing technology to support our precision location aware applications and solutions, but also that we make sensible use of location data to improve customer processes.
Corvanta Corporate Profile
Corvanta is a market leader of location-based Smart Factory Solutions which enables companies to optimise their business processes. By keeping track of key assets, Corvanta solutions bring clarity to complex operations in industries while also improving quality and reliability. Corvanta uses a unique combination of advancefd industry knowledge and an experienced team to deliver effective and superior solutions that offer unprecedented visibility, control and accuracy, delivering time and cost savings. Corvanta solutions are easy to implement and flexible to a particular business’s needs, no matter which area of the globe they operate in.
Corvanta offers two location-oriented products; RTLS (Real-time Location Solutions) and Geospatial Systems and operates in a number of industries ranging from manufacturing and utilities to telecommunications and is used by a number of blue chip customers across the world, such as KLT, Skyvane, Groundmole, Fenwick Power, RAL and Nordische Fernmelde.
Corvanta Corporate Colours
Orange:
Pantone 021C
R: 237 / G: 110 / B: 0
C: 0 / M: 53 / Y: 100 / K: 0
Hex #ED6E00
Dark Blue:
Pantone 662C
R: 15 / G: 31 / B: 122
C: 100 / M: 71 / Y: 0 / K:0
Hex #0F1F7A
Light Blue:
Pantone 300C
R: 0 / G: 110 / B: 199
C: 100 / M: 44 / Y: 0 / K:0
Hex #006EC7
Corvanta Corporate Fonts
The preferred font is Tahoma for Title, Topics and Print. In certain situations, Arial is an acceptable alternative.
Target Market(s)
Manufacturing industry, Automotive and Aerospace
Industry/Entity Type
Telecommunications
Look and feel

```html
<!DOCTYPE html>
<html lang="en">
<head>
<meta charset="utf-8">
<title>Corvanta – Presentation Template Page 4</title>
<link rel="stylesheet" href="https://fonts.googleapis.com/css2?family=Noto+Sans:ital,wght@0,400;0,700;0,800;0,900;1,700&family=Noto+Serif:wght@700&family=Open+Sans:wght@400;600;700&family=Carlito&display=swap">
<style>
  :root {
    --bg-top: #ebe8da;
    --bg-bottom: #f9f7ef;
    --ink-dark: #3a3a3a;
    --ink-mid: #555555;
    --accent-yellow: #f7c400;
    --accent-gold: #ffb300;
    --bar-light: #ffcc00;
    --bar-dark: #dba700;
    --bar-edge: #a87f00;
    --grid: #8a8a8a;
    --footer: #2f2f33;
    --footer-box: #3b3b40;
    --brand-blue: #1f5fa9;
    --brand-orange: #f08a00;
    --white: #ffffff;
  }
  * { margin: 0; padding: 0; box-sizing: border-box; }
  html, body { width: 1200px; height: 900px; overflow: hidden; }
  body {
    position: relative;
    background: linear-gradient(to bottom, var(--bg-top) 0%, var(--bg-bottom) 70%);
    font-family: "Open Sans", Arial, sans-serif;
    color: var(--ink-mid);
  }
  .web-address {
    position: absolute; left: 953px; top: 36px;
    font-family: "Noto Serif", Georgia, serif; font-weight: 700; font-size: 17px;
    color: var(--ink-dark);
  }
  .web-address .brand-part { color: var(--accent-gold); }
  .page-title {
    position: absolute; left: 62px; top: 50px;
    font-family: "Noto Sans", Tahoma, sans-serif; font-weight: 900;
    color: var(--ink-dark); line-height: 68px; letter-spacing: -1px;
  }
  .page-title .line-one { display: block; font-size: 80px; }
  .page-title .line-two { display: block; font-size: 74px; }
  .page-title .page-tag { color: var(--accent-yellow); }
  .subtitle {
    position: absolute; left: 64px; top: 206px;
    font-family: "Noto Sans", Tahoma, sans-serif; font-weight: 700; font-size: 25px;
    color: var(--ink-dark);
  }
  .chart { position: absolute; left: 0; top: 0; }
  .chart text { font-family: "Carlito", Calibri, sans-serif; font-size: 15px; fill: #222; }
  .topics { position: absolute; left: 758px; top: 238px; width: 294px; }
  .topic { margin-bottom: 21px; }
  .topic-heading {
    font-family: "Noto Sans", Tahoma, sans-serif; font-weight: 700; font-size: 23px;
    color: var(--ink-mid); line-height: 36px;
  }
  .topic-text { font-size: 15px; line-height: 26.5px; text-align: justify; text-align-last: left; }
  .footer-band {
    position: absolute; left: 0; top: 780px; width: 1200px; height: 97px;
    background: var(--footer);
    box-shadow: 0 -2px 4px rgba(0,0,0,.25);
  }
  .accent-band {
    position: absolute; left: 0; top: 877px; width: 1200px; height: 23px;
    background: var(--accent-gold);
  }
  .brand-name {
    position: absolute; left: 28px; top: 808px;
    display: flex; align-items: center; gap: 10px;
    font-family: "Open Sans", Arial, sans-serif; font-weight: 600; font-size: 29px;
    color: var(--brand-blue);
  }
  .brand-dot { width: 28px; height: 28px; border-radius: 50%; background: var(--brand-orange); }
  .pager {
    position: absolute; left: 518px; top: 813px;
    display: flex; align-items: center; gap: 10px;
  }
  .pager-arrow { width: 21px; height: 21px; display: block; }
  .pager-box {
    width: 41px; height: 34px; border-radius: 4px;
    background: var(--footer-box); border: 1px solid #1f1f22;
    display: flex; align-items: center; justify-content: center;
    font-family: "Noto Sans", Tahoma, sans-serif; font-weight: 700; font-size: 17px;
  }
  .pager-box.current { color: var(--accent-yellow); }
  .pager-box.total { color: #9a9a9a; }
  .pager-of {
    font-family: "Noto Sans", Tahoma, sans-serif; font-style: italic; font-weight: 700;
    font-size: 17px; color: #8a8a8a;
  }
  .contact {
    position: absolute; left: 896px; top: 802px;
    font-size: 13.5px; line-height: 18.5px; color: var(--white);
  }
  .contact-title { color: var(--accent-gold); font-weight: 600; }
</style>
</head>
<body>
  <div class="web-address">www.<span class="brand-part">corvanta-example</span>.net</div>

  <h1 class="page-title">
    <span class="line-one">SOMETHING</span>
    <span class="line-two">TITLE <span class="page-tag">Pg4</span></span>
  </h1>
  <p class="subtitle">Write some lines about your business</p>

  <svg class="chart" width="620" height="740" viewBox="0 0 620 740" aria-label="Bar chart of business areas">
    <g stroke="var(--grid)" stroke-width="1">
      <line x1="108" y1="302" x2="598" y2="302"/>
      <line x1="108" y1="345" x2="598" y2="345"/>
      <line x1="108" y1="388" x2="598" y2="388"/>
      <line x1="108" y1="431" x2="598" y2="431"/>
      <line x1="108" y1="474" x2="598" y2="474"/>
      <line x1="108" y1="517" x2="598" y2="517"/>
      <line x1="108" y1="560" x2="598" y2="560"/>
      <line x1="108" y1="603" x2="598" y2="603"/>
      <line x1="108" y1="646" x2="598" y2="646"/>
      <line x1="108" y1="689" x2="598" y2="689"/>
      <line x1="108" y1="302" x2="108" y2="689"/>
      <line x1="108" y1="689" x2="108" y2="695"/>
      <line x1="232" y1="689" x2="232" y2="695"/>
      <line x1="354" y1="689" x2="354" y2="695"/>
      <line x1="476" y1="689" x2="476" y2="695"/>
      <line x1="598" y1="689" x2="598" y2="695"/>
    </g>
    <g text-anchor="end">
      <text x="96" y="307">9</text><text x="96" y="350">8</text><text x="96" y="393">7</text>
      <text x="96" y="436">6</text><text x="96" y="479">5</text><text x="96" y="522">4</text>
      <text x="96" y="565">3</text><text x="96" y="608">2</text><text x="96" y="651">1</text>
      <text x="96" y="694">0</text>
    </g>
    <g stroke="var(--bar-edge)" stroke-width="1.5">
      <rect x="140" y="337" width="62" height="352" fill="var(--bar-light)"/>
      <rect x="262" y="552" width="62" height="137" fill="var(--bar-dark)"/>
      <rect x="384" y="629" width="62" height="60" fill="var(--bar-light)"/>
      <rect x="506" y="638" width="62" height="51" fill="var(--bar-dark)"/>
    </g>
    <g text-anchor="middle">
      <text x="171" y="721">3D</text>
      <text x="293" y="721">websites</text>
      <text x="415" y="721">advertising</text>
      <text x="537" y="721">video</text>
    </g>
  </svg>

  <section class="topics">
    <div class="topic">
      <h2 class="topic-heading">Heading</h2>
      <p class="topic-text">Lorem Ipsum has been the industry's standard dummy text ever since the 1500s.</p>
    </div>
    <div class="topic">
      <h2 class="topic-heading">Heading</h2>
      <p class="topic-text">Lorem Ipsum has been the industry's standard dummy text ever since the 1500s.</p>
    </div>
    <div class="topic">
      <h2 class="topic-heading">Heading</h2>
      <p class="topic-text">Lorem Ipsum has been the industry's standard dummy text ever since the 1500s.</p>
    </div>
    <div class="topic">
      <h2 class="topic-heading">Heading</h2>
      <p class="topic-text">Lorem Ipsum has been the industry's standard dummy text ever since .</p>
    </div>
  </section>

  <footer>
    <div class="footer-band"></div>
    <div class="accent-band"></div>
    <div class="brand-name"><span class="brand-dot"></span>Corvanta</div>
    <nav class="pager" aria-label="Page 4 of 5">
      <svg class="pager-arrow" viewBox="0 0 21 21" aria-hidden="true">
        <circle cx="10.5" cy="10.5" r="10" fill="var(--accent-gold)"/>
        <path d="M12.5 6 L8 10.5 L12.5 15" fill="none" stroke="var(--white)" stroke-width="2.4" stroke-linecap="round" stroke-linejoin="round"/>
      </svg>
      <span class="pager-box current">4</span>
      <span class="pager-of">of</span>
      <span class="pager-box total">5</span>
      <svg class="pager-arrow" viewBox="0 0 21 21" aria-hidden="true">
        <circle cx="10.5" cy="10.5" r="10" fill="var(--accent-gold)"/>
        <path d="M8.5 6 L13 10.5 L8.5 15" fill="none" stroke="var(--white)" stroke-width="2.4" stroke-linecap="round" stroke-linejoin="round"/>
      </svg>
    </nav>
    <address class="contact" style="font-style: normal;">
      <div class="contact-title">Contact Us</div>
      <div>Lorem ipsum dolor, 03663, State, Country</div>
      <div>P.&nbsp; 555 014 2290/ hello@corvanta-example.net</div>
    </address>
  </footer>
</body>
</html>
```